Project Brief: Bright Lane Works Business Card Design

I’m looking for a modern, monochromatic business card design (black and white only) that reflects the sophistication and intelligence of my company, Bright Lane Works (www.brightlaneworks.example) — a firm that helps small and medium-sized businesses automate operations and integrate AI into their workflows.

The design should communicate clarity, confidence, and innovation — clean and minimal, yet bold and professional.

Design Direction
-Color: Monochrome palette — black, white, and shades of gray only.
-Design should support matte or soft-touch finish.
-Optional: include mockups showing foil or embossed variations

Layout Concept:
-Ideally, one side white and the other black for contrast.
-Horizontal Orientation 2" x 3.5"

Typography:
-Use clean, geometric sans-serifs (e.g., Inter, Poppins, Helvetica Neue, DM Sans, etc.).

Front Side (Brand Side)
-Prominently feature the Bright Lane Works logo & Tag line(attached).

Back Side (Personal Side)

Include:
-Marcus Whitaker
-Founder
-mwhitaker@brightlaneworks.example
-www.brightlaneworks.example
-Office: 555.214.3386
-Mobile: 555.281.4472
-Add a QR code that links directly to my LinkedIn profile (bottom right corner preferred). Maintain strong visual balance and readability — the QR should feel integrated, not like an afterthought.

Target Market(s)

Small/Medium Sized Business Owners

Industry/Entity Type

Consulting

Contact Information for Business Card

See Project Description

Font styles to use
Sans Serif

Colors

Designer to choose only greyscale colors for use in the design.

Requirements
Must have
• See Project Description
Nice to have
• See Project Description
Should not have
• See Project Description

```html
<!DOCTYPE html>
<html lang="en">
<head>
<meta charset="utf-8">
<title>Bright Lane Works — Business Card</title>
<link href="https://fonts.googleapis.com/css2?family=Poppins:wght@400;500;600;700&display=swap" rel="stylesheet">
<style>
  :root {
    --stage: #2b2c2e;
    --ink: #0d0d0d;
    --paper: #ffffff;
    --grey: #7a7a7a;
    --grey-light: #b4b4b4;
  }
  * { box-sizing: border-box; margin: 0; padding: 0; }
  html, body { width: 1200px; height: 952px; overflow: hidden; }
  body {
    background: var(--stage);
    font-family: "Poppins", sans-serif;
    position: relative;
  }
  .card {
    position: absolute;
    width: 560px;
    height: 320px;
    box-shadow: 0 18px 40px rgba(0,0,0,.45);
  }
  .card--brand { left: 560px; top: 120px; background: var(--ink); color: var(--paper); }
  .card--personal { left: 90px; top: 500px; background: var(--paper); color: var(--ink); }

  .wordmark { position: absolute; display: flex; flex-direction: column; }
  .wordmark__row { display: flex; align-items: center; gap: 12px; }
  .wordmark__name { font-weight: 600; letter-spacing: -.2px; white-space: nowrap; }
  .wordmark__square { background: currentColor; flex: none; }
  .wordmark__tagline { font-weight: 500; letter-spacing: 3px; text-transform: uppercase; }

  .card--brand .wordmark { left: 120px; top: 118px; }
  .card--brand .wordmark__name { font-size: 34px; }
  .card--brand .wordmark__square { width: 20px; height: 20px; }
  .card--brand .wordmark__tagline { font-size: 10px; margin-top: 4px; }

  .card--personal .wordmark { left: 40px; top: 60px; }
  .card--personal .wordmark__name { font-size: 24px; }
  .card--personal .wordmark__square { width: 15px; height: 15px; }
  .card--personal .wordmark__tagline { font-size: 7.5px; margin-top: 3px; letter-spacing: 2.4px; }

  .rule-grey { position: absolute; left: 22px; top: 262px; width: 270px; height: 4px; background: var(--grey-light); }
  .rule-black { position: absolute; left: 292px; top: 260px; width: 250px; height: 8px; background: var(--ink); }

  .person { position: absolute; left: 298px; top: 108px; }
  .person__name { font-size: 17px; font-weight: 700; letter-spacing: .4px; text-transform: uppercase; line-height: 1.1; }
  .person__role { font-size: 12px; color: var(--grey); margin-top: 1px; }
  .person__divider { width: 52px; height: 1px; background: var(--grey); margin-top: 6px; }

  .contacts { position: absolute; left: 250px; top: 170px; list-style: none; }
  .contacts li { display: flex; align-items: center; gap: 8px; height: 20px; font-size: 11px; color: #5a5a5a; }
  .contacts svg { width: 13px; height: 13px; flex: none; }
</style>
</head>
<body>
  <section class="card card--brand" aria-label="Brand side">
    <div class="wordmark">
      <div class="wordmark__row">
        <span class="wordmark__name">Bright Lane Works</span>
        <span class="wordmark__square"></span>
      </div>
      <span class="wordmark__tagline">Intelligent Automation</span>
    </div>
  </section>

  <section class="card card--personal" aria-label="Personal side">
    <div class="wordmark">
      <div class="wordmark__row">
        <span class="wordmark__name">Bright Lane Works</span>
        <span class="wordmark__square"></span>
      </div>
      <span class="wordmark__tagline">Intelligent Automation</span>
    </div>

    <div class="person">
      <p class="person__name">Marcus Whitaker</p>
      <p class="person__role">Founder</p>
      <div class="person__divider"></div>
    </div>

    <ul class="contacts">
      <li>
        <svg viewBox="0 0 14 14"><rect width="14" height="14" rx="2.5" fill="#111"/><path d="M4 3.2l1.6-.2.8 2-1 .8c.5 1.1 1.3 1.9 2.4 2.4l.8-1 2 .8-.2 1.6c-3.6.2-6.6-2.8-6.4-6.4z" fill="#fff"/></svg>
        <span>555.281.4472</span>
      </li>
      <li>
        <svg viewBox="0 0 14 14"><rect width="14" height="14" rx="2.5" fill="#111"/><rect x="3.5" y="3" width="4" height="8" rx=".6" fill="#fff"/><rect x="8.3" y="4.5" width="2.4" height="6.5" fill="#fff"/></svg>
        <span>555.214.3386</span>
      </li>
      <li>
        <svg viewBox="0 0 14 14"><rect width="14" height="14" rx="2.5" fill="#111"/><rect x="3" y="4.2" width="8" height="5.6" fill="#fff"/><path d="M3 4.2l4 3.2 4-3.2" fill="none" stroke="#111" stroke-width=".9"/></svg>
        <span>mwhitaker@brightlaneworks.example</span>
      </li>
      <li>
        <svg viewBox="0 0 14 14"><rect width="14" height="14" rx="2.5" fill="#111"/><circle cx="7" cy="7" r="3.8" fill="none" stroke="#fff" stroke-width=".9"/><path d="M3.2 7h7.6M7 3.2c-1.6 2.2-1.6 5.4 0 7.6M7 3.2c1.6 2.2 1.6 5.4 0 7.6" fill="none" stroke="#fff" stroke-width=".8"/></svg>
        <span>www.brightlaneworks.example</span>
      </li>
    </ul>

    <div class="rule-grey"></div>
    <div class="rule-black"></div>
  </section>
</body>
</html>
```